MODELS AGENCY NEW YEAR 2026 CARD

A 10 cm x 21 cm horizontal New Year card for clients of our 2 models agencies, Pommelin (kids) and Velvaride (actors and adults) (logo in the jobs).

Side A of the card: creative mission:
-text: 2026
-text: Peace and Love
-Studio or movie set atmosphere
-tone of voice: optimistic, positive, colorful

Side B:
(name of 4 people of the agency:)
Odette, Anne-Sophie, Hortense & Luc-Antoine,
(2 logos)
Pommelin & VelvaRide
(Adres)
Rue des Tilleuls 74 b3 - 1200 Bruxelles - Belgique

Target Market(s)

Movie directors, photographers

Industry/Entity Type

Fashion, advertising & Movies

Requirements
Must have
• SEE TEXT IN BRIEFING

```html
<!DOCTYPE html>
<html lang="fr">
<head>
<meta charset="utf-8">
<title>Carte de vœux 2026 – Velvaride &amp; Pommelin</title>
<link rel="stylesheet" href="https://fonts.googleapis.com/css2?family=Allura&family=Outfit:wght@300;400;600&family=Quicksand:wght@300&display=swap">
<style>
  :root {
    --backdrop: #cccccc;
    --purple: #3d1a63;
    --orange: #f26229;
    --teal: #5fd3d6;
    --white: #ffffff;
    --neon: #3fb2ef;
    --sky: #d6f0fc;
  }
  * { margin: 0; padding: 0; box-sizing: border-box; }
  html, body { width: 1131px; height: 1200px; overflow: hidden; background: var(--backdrop); }
  body { position: relative; font-family: "Outfit", sans-serif; }

  .card-side { position: absolute; left: 130px; width: 870px; height: 414px; overflow: hidden; }
  .side-front { top: 175px; }
  .side-back { top: 610px; background: var(--white); }

  .studio-scene {
    position: absolute; inset: 0;
    background:
      radial-gradient(ellipse 22% 30% at 45% 48%, #e9a7d8 0%, rgba(233,167,216,0) 100%),
      radial-gradient(ellipse 30% 45% at 28% 55%, rgba(40,110,220,.75) 0%, rgba(40,110,220,0) 100%),
      radial-gradient(ellipse 25% 40% at 60% 55%, rgba(230,90,50,.7) 0%, rgba(230,90,50,0) 100%),
      linear-gradient(90deg, #0d1a3a 0%, #1a1f4d 35%, #2a1436 60%, #2b1258 80%, #1c0c3c 100%);
  }
  .front-art { position: absolute; inset: 0; }

  .watercolor-wash {
    position: absolute; inset: 0;
    background:
      radial-gradient(ellipse 45% 40% at 35% 20%, #bfe6fa 0%, rgba(191,230,250,0) 100%),
      radial-gradient(ellipse 35% 35% at 70% 15%, #c9ecfb 0%, rgba(201,236,251,0) 100%),
      linear-gradient(180deg, var(--sky) 0%, #eef9fe 60%, #ffffff 100%);
  }
  .back-art { position: absolute; inset: 0; }

  .team-names {
    position: absolute; left: 62px; top: 94px;
    font-weight: 300; font-size: 31px; line-height: 42px; color: var(--purple);
  }
  .address {
    position: absolute; left: 88px; top: 324px;
    font-weight: 300; font-size: 20px; line-height: 27px; color: var(--white);
  }
  .address-pin { position: absolute; left: -22px; top: 4px; width: 16px; height: 16px; }

  .agency-panel {
    position: absolute; left: 590px; top: 37px; width: 218px; height: 341px;
    background: var(--white); border: 5px solid var(--orange); border-radius: 12px;
    text-align: center; color: var(--purple);
  }
  .agency { position: absolute; left: 0; right: 0; }
  .agency-adults { top: 62px; }
  .agency-kids { top: 218px; }
  .agency-name { font-weight: 600; font-size: 27px; line-height: 30px; letter-spacing: 0.5px; }
  .agency-tagline { font-weight: 400; font-size: 7.5px; letter-spacing: 1px; margin-top: 3px; }
  .agency-since { font-weight: 400; font-size: 5.5px; letter-spacing: .5px; margin-top: 22px; }
</style>
</head>
<body>

<section class="card-side side-front">
  <div class="studio-scene" role="img" aria-label="Photo studio at night with a lit backdrop, softboxes and blue and orange coloured lights"></div>
  <svg class="front-art" width="870" height="414" viewBox="0 0 870 414">
    <g class="ribbon" fill="none">
      <path d="M 425 430 C 490 330, 540 190, 640 110 S 790 5 880 -4" stroke="var(--orange)" stroke-width="40"/>
      <path d="M 425 430 C 490 330, 540 190, 640 110 S 790 5 880 -4" stroke="var(--white)" stroke-width="20"/>
      <path d="M 425 430 C 490 330, 540 190, 640 110 S 790 5 880 -4" stroke="var(--teal)" stroke-width="10"/>
    </g>
    <circle cx="570" cy="212" r="130" fill="var(--orange)"/>
    <circle cx="590" cy="228" r="128" fill="var(--teal)"/>
    <circle cx="579" cy="214" r="118" fill="var(--white)"/>
    <circle cx="579" cy="214" r="112" fill="#1e0b2e"/>

    <g class="greeting" fill="var(--white)" font-family="Allura, cursive">
      <text x="502" y="214" font-size="78" textLength="138" lengthAdjust="spacingAndGlyphs">Peace</text>
      <text x="527" y="257" font-size="26" textLength="30" lengthAdjust="spacingAndGlyphs">and</text>
      <text x="558" y="276" font-size="74" textLength="92" lengthAdjust="spacingAndGlyphs">Love</text>
    </g>

    <g class="year" font-family="Quicksand, sans-serif" font-weight="300" font-size="120" style="filter: drop-shadow(0 0 6px #3fb2ef);">
      <text x="139" y="378" fill="none" stroke="var(--neon)" stroke-width="6" textLength="241" lengthAdjust="spacingAndGlyphs">2026</text>
      <text x="139" y="378" fill="none" stroke="#c8ecff" stroke-width="1.5" textLength="241" lengthAdjust="spacingAndGlyphs">2026</text>
    </g>
  </svg>
</section>

<section class="card-side side-back">
  <div class="watercolor-wash" role="img" aria-label="Soft light blue watercolour wash"></div>
  <svg class="back-art" width="870" height="414" viewBox="0 0 870 414">
    <polygon points="0,296 870,268 870,278 0,306" fill="var(--orange)"/>
    <polygon points="0,306 870,278 870,414 0,414" fill="var(--purple)"/>
  </svg>

  <div class="team-names">Odette,<br>Anne-Sophie,<br>Hortense &amp;<br>Luc-Antoine</div>

  <div class="address">
    <svg class="address-pin" viewBox="0 0 16 16"><circle cx="8" cy="8" r="7.5" fill="var(--white)"/><circle cx="8" cy="6.3" r="2.4" fill="var(--purple)"/><path d="M3.8 12.5 C4.8 9.8 11.2 9.8 12.2 12.5 Z" fill="var(--purple)"/></svg>
    Rue des Tilleuls 74 b3 - 1200<br>Bruxelles - Belgique
  </div>

  <div class="agency-panel">
    <div class="agency agency-adults">
      <div class="agency-name">VelvaRide</div>
      <div class="agency-tagline">PEOPLE, ACTORS &amp; MODELS AGENCY</div>
      <div class="agency-since">– SINCE 2000 –</div>
    </div>
    <div class="agency agency-kids">
      <div class="agency-name">Pommelin</div>
      <div class="agency-tagline">CHILDREN MODELS AGENCY</div>
      <div class="agency-since">– SINCE 1982 –</div>
    </div>
  </div>
</section>

</body>
</html>
```